A 500th Reformation Anniversary book

I am in need of a front and back cover design.
Front Cover:
The title is "KEEP IT SAFE -Edwin Harrow". It is an autobiography written as a biography. Harrow refers to this book's title in the respect that the book should be thrown into a bonfire and destroyed. Since this is a major part of the climax to the book, and since Harrow refers to the title and the cover photo, some type of fire photo is requested. In my working stage, I used a photograph that I had taken on our property.
Back Cover:
I would like a continuation in color from the front. The back will have the typical ISBN, etc. but also a short description of the book and two endorsements.
The final cover will need to be available for the following:
This book will have three formats. The book will be:
8.5" x 11" spiral bound - no spine
8.5" x 5.5" perfect bound
ebook
I do not have the exact spine width, but the page count for the perfect bound is 190.
I have confirmed that I will receive final copy that I can work with. I will need to add "School Edition" to the cover for the Spiral Bound.
I believe that's everything you need!
Thank you!
T.E.Voss

Target Market(s)

Middle School-Aged Children through Adults

Font styles to use
Sans Serif

Requirements
Must have
• See Project description plus...
• Title should be written such that it is clear that the 'Edwin Harrow' part of it is simply a byline to the words KEEP IT SAFE.

```html
<!DOCTYPE html>
<html lang="en">
<head>
<meta charset="utf-8">
<title>KEEP IT SAFE – Edwin Harrow – Cover</title>
<link href="https://fonts.googleapis.com/css2?family=Exo+2:wght@400;500;600&display=swap" rel="stylesheet">
<style>
  :root {
    --ink-dark: #1b1012;
    --night: #0e0605;
    --ember-band: #c84a2e;
    --flame-core: #ffc040;
    --flame-mid: #f07a12;
    --flame-deep: #5a1806;
    --veil: rgba(80, 70, 58, 0.55);
    --title-veil: rgba(40, 28, 24, 0.6);
    --paper-white: #ffffff;
  }
  html, body {
    margin: 0;
    padding: 0;
    width: 1200px;
    height: 883px;
    overflow: hidden;
    background: var(--ink-dark);
  }
  .cover-spread {
    position: relative;
    width: 1200px;
    height: 883px;
    background: var(--ink-dark);
    font-family: "Exo 2", sans-serif;
    color: var(--paper-white);
    overflow: hidden;
  }
  .fire-photo {
    position: absolute;
    top: 0;
    height: 842px;
    background-color: var(--night);
  }
  .fire-photo.back {
    left: 28px;
    width: 538px;
    background-image:
      radial-gradient(ellipse 28% 18% at 52% 14%, var(--flame-core), transparent 75%),
      radial-gradient(ellipse 40% 26% at 45% 18%, var(--flame-mid), transparent 80%),
      radial-gradient(ellipse 45% 20% at 55% 88%, var(--flame-core), transparent 75%),
      radial-gradient(ellipse 60% 35% at 55% 82%, var(--flame-mid), transparent 80%),
      radial-gradient(ellipse 70% 30% at 50% 100%, var(--flame-deep), transparent 90%);
  }
  .fire-photo.front {
    left: 629px;
    width: 538px;
    background-image:
      radial-gradient(ellipse 26% 20% at 42% 16%, var(--flame-core), transparent 75%),
      radial-gradient(ellipse 40% 30% at 50% 20%, var(--flame-mid), transparent 80%),
      radial-gradient(ellipse 42% 24% at 50% 78%, var(--flame-core), transparent 75%),
      radial-gradient(ellipse 60% 40% at 50% 75%, var(--flame-mid), transparent 82%),
      radial-gradient(ellipse 70% 30% at 50% 100%, var(--flame-deep), transparent 90%);
  }
  .spine {
    position: absolute;
    left: 571px;
    top: 0;
    width: 51px;
    height: 883px;
    background: var(--ink-dark);
  }
  .spine-title {
    position: absolute;
    left: 600px;
    top: 760px;
    transform-origin: 0 0;
    transform: rotate(-90deg) translateY(-50%);
    white-space: nowrap;
    font-size: 38px;
    font-weight: 500;
    line-height: 1;
    letter-spacing: -0.01em;
  }
  .spine-title .byline {
    font-size: 26px;
    letter-spacing: 0.26em;
  }
  .ember-band {
    position: absolute;
    top: 842px;
    height: 41px;
    background: var(--ember-band);
  }
  .ember-band.back { left: 0; width: 571px; }
  .ember-band.front { left: 622px; width: 578px; }
  .blurb-panel {
    position: absolute;
    left: 118px;
    top: 181px;
    width: 388px;
    height: 463px;
    background: var(--veil);
  }
  .blurb-text {
    position: absolute;
    left: 134px;
    top: 218px;
    width: 338px;
    margin: 0;
    font-size: 13px;
    font-weight: 500;
    line-height: 17.3px;
    letter-spacing: 0.3em;
    text-align: justify;
  }
  .blurb-text .section-label { display: block; text-align: left; }
  .title-band {
    position: absolute;
    left: 629px;
    top: 260px;
    width: 457px;
    height: 178px;
    background: var(--title-veil);
  }
  .front-title {
    position: absolute;
    left: 790px;
    top: 318px;
    margin: 0;
    font-size: 40px;
    font-weight: 600;
    line-height: 1;
    letter-spacing: -0.02em;
  }
  .front-byline {
    position: absolute;
    left: 806px;
    top: 358px;
    margin: 0;
    font-size: 23px;
    font-weight: 500;
    letter-spacing: 0.27em;
    line-height: 1;
  }
</style>
</head>
<body>
  <main class="cover-spread">
    <div class="fire-photo back" role="img" aria-label="Photograph of bonfire flames rising against a black night background"></div>
    <div class="fire-photo front" role="img" aria-label="Photograph of bonfire flames rising against a black night background"></div>

    <div class="blurb-panel"></div>
    <p class="blurb-text">Edwin Harrow tells his own life as if it belonged to someone else, from a quiet farm to a crowded hall. Every page asks one thing of the reader: when you are done, keep it safe, or give it to the fire.
      <span class="section-label">Praise:</span>
      "A bold and honest voice for young readers and old alike." -Clara Wend
      <span class="section-label">&nbsp;</span>
      "I could not put it down until the last ember was out." -Jonah Pike
      <span class="section-label">&nbsp;</span>
      <span class="section-label">ISBN 978-0-00-000000-0</span></p>

    <div class="spine"></div>
    <div class="spine-title">KEEP IT SAFE <span class="byline">- Edwin Harrow</span></div>

    <div class="title-band"></div>
    <h1 class="front-title">KEEP IT SAFE</h1>
    <p class="front-byline">-Edwin Harrow</p>

    <div class="ember-band back"></div>
    <div class="ember-band front"></div>
  </main>
</body>
</html>
```